PowerPoint Design

We require a sample PowerPoint design so we can pitch PPT design services to a client.

The designs do NOT need to be done in PowerPoint, but should reflect designs that *could* be created in PPT format.

We require 3 slides as part of this project:

1. A slide containing the statistical chart based on data in Figure 3.3 at http://www7.dovrimark.org/survey-releves/2006/tb-qr/ab-cd/index.cfm?LANG=ENG&VIEW=C&format=flash&PRCODE=01&TOPIC_ID=2
-> note, don't just copy and paste the existing graph - come up with something innovative and eye catching

2. Inspirational slide to motivate employees. Zorvex "inspirational quote" and select a quote you think is appropriate. Imagery should generate enthusiasm/optimism.

3. A slide of your own choosing.
Updates

Project Deadline Extended
Reason: One of the team reviewing the designs is away from office. We've decided to give other designers a chance to submit ideas. Final decision will be made on December 5th, 2011.

Target Market(s)

Business professionals

Industry/Entity Type

Zorvex

Requirements
Must have
• Must have 3 slides.

```html
<!DOCTYPE html>
<html lang="en">
<head>
<meta charset="utf-8">
<title>Inspirational Slide – Working Together</title>
<link rel="stylesheet" href="https://fonts.googleapis.com/css2?family=Open+Sans:ital,wght@0,400;0,700;1,700&display=swap">
<style>
  :root {
    --navy-deep: #0a1628;
    --navy: #1f4d85;
    --blue: #3f7fcc;
    --blue-light: #7eb0ea;
    --sky-pale: #cfe1f7;
    --white: #ffffff;
    --logo-blue: #86b6ee;
    --suit-dark: #2a2d33;
    --shirt-light: #eef1f5;
    --skin-warm: #d9b79a;
    --soil: #3a2f27;
    --leaf: #8cc63f;
    --sky: #2f7fdc;
    --cloud: #e8f1fb;
    --glass: #5f88b8;
  }
  * { margin: 0; padding: 0; box-sizing: border-box; }
  html, body { width: 1200px; height: 900px; overflow: hidden; }
  body { font-family: "Open Sans", "Segoe UI", Arial, sans-serif; }

  .slide {
    position: relative;
    width: 1200px;
    height: 900px;
    overflow: hidden;
    background:
      radial-gradient(ellipse 70% 25% at 50% 56%, rgba(160,200,240,0.35), transparent 70%),
      linear-gradient(125deg, var(--navy-deep) 0%, var(--navy) 22%, var(--blue) 50%, var(--blue-light) 78%, var(--sky-pale) 100%);
  }

  .quote {
    position: absolute;
    left: 90px;
    width: 1000px;
    top: 134px;
    text-align: center;
    color: var(--white);
    font-weight: 700;
    font-style: italic;
    font-size: 50px;
    line-height: 72px;
  }

  .attribution {
    position: absolute;
    right: 210px;
    top: 366px;
    color: var(--white);
    font-weight: 400;
    font-size: 27px;
    line-height: 38px;
    letter-spacing: 2.5px;
  }

  .image-strip {
    position: absolute;
    left: 0;
    top: 483px;
    width: 1200px;
    height: 252px;
    display: flex;
    box-shadow: 0 -6px 18px rgba(10,30,60,0.25), 0 6px 18px rgba(10,30,60,0.25);
  }
  .image-strip .photo { height: 100%; }
  .photo--team {
    width: 403px;
    background:
      radial-gradient(circle at 45% 50%, var(--skin-warm) 0%, #c9a88c 22%, var(--shirt-light) 46%, #b8bec8 66%, var(--suit-dark) 100%);
  }
  .photo--growth {
    width: 393px;
    background:
      linear-gradient(180deg, var(--white) 0%, var(--white) 40%, #e6f2d2 58%, #b9d98a 66%, #6b5a4a 76%, var(--soil) 82%, #f4f4f2 90%, var(--white) 100%);
  }
  .photo--skyline {
    width: 404px;
    background:
      linear-gradient(100deg, var(--sky) 0%, var(--cloud) 22%, var(--sky) 38%, var(--glass) 45%, #a9c6e6 62%, var(--glass) 78%, var(--sky) 90%, #b58a62 100%);
  }

  .logo {
    position: absolute;
    left: 1038px;
    top: 788px;
    color: var(--logo-blue);
    font-weight: 700;
    font-size: 44px;
    line-height: 37px;
    letter-spacing: -2px;
  }
</style>
</head>
<body>
  <main class="slide">
    <blockquote class="quote">”Coming together is a beginning;<br>keeping together is progress;<br>working together is success.”</blockquote>
    <p class="attribution">HARLAN FROST</p>

    <section class="image-strip">
      <div class="photo photo--team" role="img" aria-label="Smiling business team in a huddle seen from below"></div>
      <div class="photo photo--growth" role="img" aria-label="Three green seedlings of increasing size growing from small mounds of soil"></div>
      <div class="photo photo--skyline" role="img" aria-label="Glass office tower reflecting white clouds against a bright blue sky"></div>
    </section>

    <div class="logo">YOUR<br>LOGO</div>
  </main>
</body>
</html>
```